Business card design for immigration consulting business

We need business card design for a company called T&R Migration Advisors Inc. This is a boutique immigration consulting and foreign recruitment agency owned and managed by two partners.
The business card will be used by partners \ owners of the business. The best way to describe the business would be committed to client, passionate about providing top-notch services, engaging, competent, professional

Target Market(s)

We work with individuals in and outside of Canada who need immigration advise as well as Canadian businesses looking to hire or sponsor foreign workers to Canada

Industry/Entity Type

Consulting

Contact Information for Business Card

The business card should have a standard size and horizontal lay-out

Font styles to use
Serif

Colors
f04a50
ec1f27
cbcbcb
dbdbdb

Requirements
Must have
• The business card mush have our logo, name of the company first and last name of the partner, position, phone, cell, fax, e-mail, skype, web-site
• Our first choice would a classic design with minimalist looks and elegant fonts and colors, but we are open minded to any creative ideas too
Nice to have
• On the other side it may have the description of the company: Immigration and Foreign Recruitment Services
• We're considering using stamping \ lettering on our business cards
• It would be nice if the business card would have white space, in case someone would like to make notes on it.
• One (back side) side of the business card can be all red with white logo
Should not have
• We do not want to have our pictures on the business card
• We do no want to have Canadian maple leaf on the business card as we already have one in our logo

```html
<!DOCTYPE html>
<html lang="en">
<head>
<meta charset="utf-8">
<title>T&amp;R Migration Advisors – Business Card</title>
<link rel="stylesheet" href="https://fonts.googleapis.com/css2?family=Work+Sans:wght@400;500&display=swap">
<style>
  :root {
    --backdrop: #2b2b2b;
    --card-dark: #141414;
    --card-mid: #1f1f1f;
    --white: #ffffff;
    --red: #ec1f27;
    --red-soft: #f04a50;
    --grey: #cbcbcb;
    --grey-light: #dbdbdb;
  }
  * { margin: 0; padding: 0; box-sizing: border-box; }
  html, body {
    width: 1200px; height: 900px; overflow: hidden;
    background: var(--backdrop);
    font-family: "Work Sans", Arial, sans-serif;
  }
  .canvas {
    width: 1200px; height: 900px;
    display: flex; flex-direction: column; align-items: center; justify-content: center;
    gap: 40px;
  }
  .card {
    width: 700px; height: 400px;
    background: linear-gradient(135deg, var(--card-dark) 0%, var(--card-mid) 100%);
    position: relative;
    display: flex; align-items: center;
  }
  .card--front { justify-content: center; }
  .brand {
    display: flex; align-items: center; gap: 14px;
    color: var(--white);
    font-weight: 500;
    white-space: nowrap;
  }
  .brand__dot {
    width: 14px; height: 14px; border-radius: 50%;
    background: var(--red);
    flex: none;
  }
  .card--front .brand { font-size: 52px; letter-spacing: 1px; }
  .card--back { padding: 0 0 0 50px; }
  .card--back .brand { font-size: 34px; width: 300px; }
  .divider {
    width: 2px; height: 150px; margin: 0 34px 0 18px;
    background: linear-gradient(to bottom, transparent, var(--grey-light) 50%, transparent);
  }
  .contact { color: var(--white); }
  .contact__name {
    color: var(--red);
    font-size: 25px; font-weight: 500; letter-spacing: 1.5px;
    text-transform: uppercase;
  }
  .contact__role { color: var(--grey); font-size: 16px; margin: 2px 0 14px; }
  .contact__address { font-size: 17px; line-height: 1.3; margin-bottom: 10px; }
  .contact__line {
    display: flex; align-items: center; gap: 10px;
    font-size: 17px; line-height: 1.45;
  }
  .contact__line svg { width: 12px; height: 12px; flex: none; }
  .accent { color: var(--red); }
</style>
</head>
<body>
<main class="canvas">
  <section class="card card--front" aria-label="Card front">
    <div class="brand"><span class="brand__dot"></span>T&amp;R Migration</div>
  </section>

  <section class="card card--back" aria-label="Card back">
    <div class="brand"><span class="brand__dot"></span>T&amp;R Migration</div>
    <div class="divider"></div>
    <div class="contact">
      <p class="contact__name">Daniel Brooks</p>
      <p class="contact__role">Owners</p>
      <p class="contact__address">4780 Rue Laurier Ouest,<br>Montreal, Qc H2T 2B6</p>
      <p class="contact__line">
        <svg viewBox="0 0 12 12" aria-hidden="true"><path d="M2.5 1h2l1 3-1.3 1a6 6 0 0 0 2.8 2.8l1-1.3 3 1v2a1 1 0 0 1-1 1A9.5 9.5 0 0 1 1.5 2a1 1 0 0 1 1-1z" fill="var(--red)"/></svg>
        514.555.0142
      </p>
      <p class="contact__line">
        <svg viewBox="0 0 12 12" aria-hidden="true"><rect x="0.75" y="2.25" width="10.5" height="7.5" fill="none" stroke="var(--red)" stroke-width="1.2"/><path d="M1 2.6 6 6.5 11 2.6" fill="none" stroke="var(--red)" stroke-width="1.2"/></svg>
        info@trmigration.ca
      </p>
      <p class="contact__line">
        <svg viewBox="0 0 12 12" aria-hidden="true"><circle cx="6" cy="6" r="5" fill="none" stroke="var(--red)" stroke-width="1.1"/><ellipse cx="6" cy="6" rx="2.2" ry="5" fill="none" stroke="var(--red)" stroke-width="1"/><path d="M1 6h10" stroke="var(--red)" stroke-width="1"/></svg>
        <span>www.<span class="accent">trmigration</span>.ca</span>
      </p>
    </div>
  </section>
</main>
</body>
</html>
```